Business Card design for leader Solar Energy company
Loreno Energy Group
Professional
Belisa Torv
CEO
Santo Domingo: Calle Olmeda Vieja #418, Edif. Torv Corporativo, Suite 512
Las Terrenas: Calle de las Brisas, Coral Vista Plaza, Suite 512
Punta Cana; Proximamente
809.741.LORE (5673)
belisa@lorenopower-example.com
www.lorenopower-example.com
Shine Bright, Spend Less, Live Sunny.
Please use this logo for the business card design.
Thank you,
-belisa
vector logo

```html
<!DOCTYPE html>
<html lang="en">
<head>
<meta charset="utf-8">
<title>Loreno Energy Group — Business Card</title>
<link href="https://fonts.googleapis.com/css2?family=Open+Sans:wght@400;600;700&display=swap" rel="stylesheet">
<style>
  :root {
    --bg: #3a3b3d;
    --card: #f7f7f6;
    --blue: #1d5a86;
    --blue-dark: #174a70;
    --green: #3f9a3a;
    --text: #333a40;
    --muted: #5b6268;
    --rule: #c9cccf;
  }
  * { margin: 0; padding: 0; box-sizing: border-box; }
  html, body { width: 1200px; height: 901px; overflow: hidden; }
  body {
    background: var(--bg);
    font-family: "Open Sans", Arial, sans-serif;
    position: relative;
  }
  .card {
    position: absolute;
    width: 640px;
    height: 366px;
    background: var(--card);
    border-radius: 14px;
    overflow: hidden;
    box-shadow: 0 10px 30px rgba(0,0,0,.35);
  }
  .card--back { left: 80px; top: 50px; }
  .card--front { left: 480px; top: 470px; }

  .brand { display: flex; align-items: center; gap: 14px; color: var(--blue); font-weight: 600; }
  .brand__dot { border-radius: 50%; background: var(--green); flex: none; }

  .card--back .brand { position: absolute; left: 0; right: 0; top: 130px; justify-content: center; font-size: 40px; letter-spacing: 2px; }
  .card--back .brand__dot { width: 34px; height: 34px; }
  .tagline {
    position: absolute; left: 0; right: 0; bottom: 56px;
    text-align: center; color: var(--green); font-size: 20px; letter-spacing: 2px;
  }

  .card--front .brand { position: absolute; left: 34px; top: 78px; font-size: 25px; letter-spacing: 1px; width: 260px; line-height: 1.15; }
  .card--front .brand__dot { width: 26px; height: 26px; }
  .divider { position: absolute; left: 318px; top: 40px; width: 1px; height: 210px; background: var(--rule); }
  .details { position: absolute; left: 336px; top: 40px; right: 20px; color: var(--text); font-size: 11.5px; line-height: 1.35; }
  .name { color: var(--blue); font-weight: 700; font-size: 20px; line-height: 1.1; }
  .role { color: var(--muted); font-size: 11px; margin-bottom: 14px; }
  .contact { margin-top: 12px; }
  .contact li { list-style: none; display: flex; align-items: center; gap: 8px; }
  .contact svg { width: 12px; height: 12px; flex: none; }
  .icon-fill { fill: var(--blue-dark); }
  .icon-mail { fill: none; stroke: var(--blue-dark); stroke-width: 2.5; }

  .band-line { position: absolute; left: 0; right: 0; bottom: 64px; height: 4px; background: var(--green); }
  .band {
    position: absolute; left: 0; right: 0; bottom: 0; height: 64px;
    background: linear-gradient(180deg, var(--blue) 0%, var(--blue-dark) 100%);
    color: #e8f0f6; font-size: 15px; letter-spacing: 3px;
    display: flex; align-items: center; padding-left: 34px;
  }
</style>
</head>
<body>
  <section class="card card--back">
    <div class="brand"><span class="brand__dot"></span><span>Loreno Energy Group</span></div>
    <p class="tagline">Shine Bright, Spend Less, Live Sunny.</p>
  </section>

  <section class="card card--front">
    <div class="brand"><span class="brand__dot"></span><span>Loreno Energy Group</span></div>
    <div class="divider"></div>
    <div class="details">
      <p class="name">Belisa Torv</p>
      <p class="role">CEO</p>
      <p>Santo Domingo: Calle Olmeda Vieja #418,<br>Edif. Torv Corporativo, Suite 512</p>
      <p>Las Terrenas: Calle de las Brisas,<br>Coral Vista Plaza, Suite 512</p>
      <p>Punta Cana; Proximamente</p>
      <ul class="contact">
        <li><svg viewBox="0 0 24 24"><path class="icon-fill" d="M6.6 10.8a15.1 15.1 0 0 0 6.6 6.6l2.2-2.2a1 1 0 0 1 1-.25 11.4 11.4 0 0 0 3.6.57 1 1 0 0 1 1 1V20a1 1 0 0 1-1 1A17 17 0 0 1 3 4a1 1 0 0 1 1-1h3.5a1 1 0 0 1 1 1c0 1.25.2 2.45.57 3.6a1 1 0 0 1-.25 1z"/></svg>809.741.LORE (5673)</li>
        <li><svg viewBox="0 0 24 24"><rect class="icon-fill" x="6" y="2" width="12" height="20" rx="2"/></svg>829.604.1187</li>
        <li><svg viewBox="0 0 24 24"><path class="icon-mail" d="M3 6h18v12H3z M3 6l9 7 9-7"/></svg>belisa@lorenopower-example.com</li>
      </ul>
    </div>
    <div class="band-line"></div>
    <div class="band">www.lorenopower-example.com</div>
  </section>
</body>
</html>
```